Clean business card with logo provided

I want a card that will stand out among the masses. I need the color and image to show professionalism and yet have a family appeal showing that I only deal with win/win scenarios. The back of the card will be used to take notes about the individual so I can use that in my database entry. I like modern design but need professionalism in it also. It needs to fit my "clean, safe, and affordable housing" motto. I need to be able to write on the file and update the card details for my employees.

Target Market(s)

Investors looking to make investment income through real estate

Industry/Entity Type

Real Estate

Contact Information for Business Card

Troy Vandemark
blank address, city, st, zip code
480-555-0147
troyvandemark@quillrentals.example
www.quillrentals.example

Font styles to use
Sans Serif

Requirements
Must have
• I would like the back of the card to have lines for info. example
• Met/Visited: Date:
• Interets:
Nice to have
• I want the cards color to match the logo background color. Font with details to be san serif and black. I want the card rectangular with square corners. Standard business card size. I would like to see cards designed with both images to see which i prefer more.

```html
<!DOCTYPE html>
<html lang="en">
<head>
<meta charset="utf-8">
<title>Quill Rentals LLC – Business Card</title>
<link rel="stylesheet" href="https://fonts.googleapis.com/css2?family=Open+Sans:wght@400;600;700&display=swap">
<style>
  :root {
    --stage: #000000;
    --teal: #00b5cc;
    --paper: #ffffff;
    --ink: #141414;
    --dots: #111111;
  }
  * { margin: 0; padding: 0; box-sizing: border-box; }
  html, body { width: 1200px; height: 900px; overflow: hidden; background: var(--stage); }
  body { position: relative; font-family: "Open Sans", Arial, sans-serif; color: var(--ink); }

  .card { position: absolute; top: 200px; width: 310px; height: 502px; }
  .card-front { left: 265px; background: var(--teal); border-radius: 58px 0 58px 0; }
  .card-back { left: 641px; background: var(--paper); border-radius: 0 58px 0 58px; }

  .brand { position: absolute; left: 36px; top: 52px; }
  .card-back .brand { left: 43px; top: 58px; }
  .brand-line { display: flex; align-items: center; gap: 8px; }
  .brand-mark { width: 12px; height: 12px; border-radius: 50%; }
  .brand-name { font-size: 24px; font-weight: 600; letter-spacing: 1px; line-height: 1; }
  .brand-tagline { margin-top: 14px; font-size: 8px; font-weight: 400; letter-spacing: 0.1px; }

  .card-front .brand-mark { background: var(--paper); }
  .card-front .brand-name { color: var(--paper); }
  .card-front .brand-tagline { color: var(--paper); }
  .card-back .brand-mark { background: var(--teal); }
  .card-back .brand-name { color: var(--teal); }
  .card-back .brand-tagline { color: var(--teal); }

  .holder-name { position: absolute; left: 31px; top: 316px; font-size: 18px; font-weight: 700; }
  .holder-address { position: absolute; left: 31px; top: 356px; font-size: 14px; line-height: 15px; }
  .contact-list { position: absolute; left: 31px; top: 404px; list-style: none; font-size: 14px; }
  .contact-list li { display: flex; align-items: center; height: 21px; }
  .contact-list svg { width: 11px; height: 11px; margin-right: 9px; fill: var(--ink); }

  .note-fields { position: absolute; left: 22px; top: 341px; width: 260px; list-style: none; }
  .note-fields li { display: flex; align-items: flex-end; height: 36px; color: var(--teal); font-size: 15px; font-weight: 600; }
  .note-fields .field-label { white-space: nowrap; margin-right: 6px; }
  .note-fields .field-line { flex: 1; border-bottom: 2px dotted var(--dots); margin-bottom: 5px; }
  .note-fields .visited { padding-left: 5px; }
  .note-fields .visited .field-line { margin-left: 10px; margin-right: 14px; }
  .note-fields .interests { padding-left: 4px; }
  .note-fields .interests .field-line { margin-right: 10px; }
</style>
</head>
<body>

<section class="card card-front" aria-label="Card front">
  <div class="brand">
    <div class="brand-line"><span class="brand-name">QUILL RENTALS LLC</span><span class="brand-mark"></span></div>
    <p class="brand-tagline">Providing clean, safe, and affordable housing</p>
  </div>
  <h1 class="holder-name">Troy Vandemark</h1>
  <p class="holder-address">12345, Address Goes Here<br>Country Name, 123456</p>
  <ul class="contact-list">
    <li><svg viewBox="0 0 24 24" aria-hidden="true"><path d="M6.6 10.8a15.1 15.1 0 0 0 6.6 6.6l2.2-2.2c.3-.3.7-.4 1-.2 1.1.4 2.3.6 3.6.6.6 0 1 .4 1 1V20c0 .6-.4 1-1 1A17 17 0 0 1 3 4c0-.6.4-1 1-1h3.5c.6 0 1 .4 1 1 0 1.3.2 2.5.6 3.6.1.3 0 .7-.2 1z"/></svg>480-555-0147</li>
    <li><svg viewBox="0 0 24 24" aria-hidden="true"><path d="M2 5h20v14H2z M4 7v1l8 5 8-5V7l-8 5z" fill-rule="evenodd"/></svg>troyvandemark@quillrentals.example</li>
    <li><svg viewBox="0 0 24 24" aria-hidden="true"><circle cx="12" cy="12" r="10"/></svg>www.quillrentals.example</li>
  </ul>
</section>

<section class="card card-back" aria-label="Card back">
  <div class="brand">
    <div class="brand-line"><span class="brand-name">QUILL RENTALS LLC</span><span class="brand-mark"></span></div>
    <p class="brand-tagline">Providing clean, safe, and affordable housing</p>
  </div>
  <ul class="note-fields">
    <li class="visited"><span class="field-label">Visited Date:</span><span class="field-line"></span></li>
    <li class="interests"><span class="field-label">Interets:</span><span class="field-line"></span></li>
    <li class="problems"><span class="field-label">Problems:</span><span class="field-line"></span></li>
  </ul>
</section>

</body>
</html>
```